Brookvale Advisors LLC web site

Brookvale Advisors LLC is a consulting and recruiting firm that provides education, perspective, guidance, and assistance to financial advisors. Dennis Halloway is the founder of this new firm and is the only employee at this time.
Please see the attached overview which will provide much narrative describing the firm, its purpose, scope of services offered, and other useful information to help you design a web site.

Target Market(s)

US based financial advisors who are looking to transition their business to an independent ( non-employee ) business model.

Industry/Entity Type

Consultant

Coding

Coded - Design and coding required

Number of Pages Required

5+ page

Font styles to use
Sans Serif

Requirements
Must have
• all relevant pages for a basic web site : Home, About, Services offered, Contact, Resources , etc.
Nice to have
• color scheme : see logo in the attached briefing document

```html
<!DOCTYPE html>
<html lang="en">
<head>
<meta charset="utf-8">
<title>Brookvale Advisors LLC</title>
<link rel="stylesheet" href="https://fonts.googleapis.com/css2?family=Poppins:wght@300;400;500;600;700&family=Marcellus&family=Cinzel:wght@400;600&display=swap">
<style>
  :root {
    --navy: #0a2748;
    --navy-deep: #061a33;
    --blue: #0f4679;
    --blue-bright: #1d6bb0;
    --ink: #1f2a37;
    --muted: #5c6672;
    --line: #d9dee4;
    --white: #ffffff;
  }
  * { box-sizing: border-box; margin: 0; padding: 0; }
  html, body { width: 1200px; height: 2616px; overflow: hidden; }
  body { font-family: "Poppins", sans-serif; color: var(--ink); background: var(--white); position: relative; }

  /* ---------- hero ---------- */
  .hero { position: absolute; top: 0; left: 0; width: 1200px; height: 600px; overflow: hidden; }
  .hero-photo {
    position: absolute; inset: 0;
    background:
      radial-gradient(ellipse 420px 300px at 820px 330px, rgba(240,168,106,.7), rgba(217,114,138,.45) 45%, rgba(15,70,121,0) 85%),
      linear-gradient(180deg, #0b2b52 0%, #173f73 45%, #3a3d77 62%, #0c2a4f 100%);
  }
  .site-nav { position: absolute; top: 0; left: 0; width: 100%; height: 96px; display: flex; align-items: center; justify-content: space-between; padding: 0 80px 0 110px; z-index: 2; }
  .brand { display: flex; align-items: center; gap: 12px; color: var(--white); font-weight: 600; font-size: 19px; letter-spacing: .5px; line-height: 1.1; }
  .brand-dot { width: 34px; height: 34px; border-radius: 50%; background: var(--white); opacity: .9; }
  .nav-links { display: flex; gap: 44px; list-style: none; }
  .nav-links a { color: var(--white); text-decoration: none; font-size: 15px; }
  .hero-copy { position: absolute; left: 110px; top: 110px; width: 560px; color: var(--white); z-index: 2; }
  .hero-title { font-weight: 700; font-size: 40px; letter-spacing: 1px; line-height: 1.1; }
  .hero-lead { margin-top: 14px; font-size: 27px; font-weight: 400; line-height: 1.4; }
  .btn-outline { display: inline-block; margin-top: 40px; border: 2px solid var(--white); border-radius: 26px; padding: 10px 38px; color: var(--white); font-size: 15px; letter-spacing: 2px; text-decoration: none; text-transform: uppercase; }
  .hero-dots { position: absolute; left: 112px; top: 474px; display: flex; gap: 8px; z-index: 2; }
  .hero-dots span { width: 14px; height: 14px; border-radius: 50%; border: 2px solid var(--white); }
  .hero-dots span.is-active { background: var(--white); }

  /* ---------- about ---------- */
  .about { position: absolute; top: 600px; left: 0; width: 1200px; height: 480px; }
  .about-text { position: absolute; left: 112px; top: 138px; width: 440px; }
  .eyebrow { font-family: "Cinzel", serif; font-size: 18px; letter-spacing: 2px; color: var(--muted); }
  .about-title { font-family: "Marcellus", serif; font-weight: 400; font-size: 40px; color: var(--blue); line-height: 1.15; margin-top: 4px; }
  .about-text p { font-size: 13.5px; line-height: 1.65; color: var(--muted); margin-top: 18px; }
  .btn-solid { display: inline-block; margin-top: 22px; background: var(--navy); color: var(--white); border-radius: 20px; padding: 8px 24px; font-size: 13px; text-decoration: none; }
  .about-photo { position: absolute; left: 600px; top: 110px; width: 488px; height: 330px; background: linear-gradient(135deg, #c9ced4, #6f7884 55%, #2b3440); }

  /* ---------- services ---------- */
  .offers { position: absolute; top: 1080px; left: 0; width: 1200px; height: 700px; }
  .offers-bg { position: absolute; inset: 0; }
  .offers-heading { position: absolute; top: 100px; width: 100%; text-align: center; color: var(--white); font-family: "Cinzel", serif; line-height: 1.2; }
  .offers-heading .small { font-size: 20px; letter-spacing: 1px; }
  .offers-heading .big { font-size: 30px; letter-spacing: 2px; }
  .offer { position: absolute; top: 180px; width: 300px; text-align: center; color: var(--white); }
  .offer-ring { position: relative; width: 240px; height: 240px; margin: 0 auto; }
  .offer-photo { position: absolute; left: 14px; top: 14px; width: 212px; height: 212px; border-radius: 50%; }
  .offer-ring svg { position: absolute; inset: 0; }
  .offer h3 { margin-top: 66px; font-family: "Cinzel", serif; font-weight: 600; font-size: 17px; letter-spacing: 1px; }
  .offer p { margin-top: 8px; font-size: 12.5px; line-height: 1.6; opacity: .9; padding: 0 14px; }
  .offer a { display: inline-block; margin-top: 8px; color: var(--white); font-family: "Cinzel", serif; font-size: 16px; letter-spacing: 1px; text-decoration: underline; }

  /* ---------- testimonials ---------- */
  .clients { position: absolute; top: 1780px; left: 0; width: 1200px; height: 560px; }
  .clients-heading { position: absolute; top: 66px; width: 100%; text-align: center; font-family: "Cinzel", serif; color: var(--blue); line-height: 1.3; }
  .clients-heading .small { font-size: 18px; }
  .clients-heading .big { font-size: 30px; font-weight: 600; letter-spacing: 2px; }
  .quote-card { position: absolute; top: 150px; width: 300px; height: 222px; background: var(--white); box-shadow: 0 4px 18px rgba(10,39,72,.16); padding: 24px 24px; }
  .quote-head { display: flex; align-items: center; gap: 14px; }
  .avatar { width: 62px; height: 62px; border-radius: 50%; background: linear-gradient(135deg, #8a6a58, #3b2b25); flex: none; }
  .quote-name { font-family: "Cinzel", serif; font-weight: 600; font-size: 16px; color: var(--ink); letter-spacing: 1px; white-space: nowrap; }
  .quote-role { font-size: 12px; color: var(--muted); }
  .quote-card p { margin-top: 14px; font-size: 12.5px; line-height: 1.6; color: var(--muted); }
  .slider-arrows { position: absolute; top: 494px; left: 544px; display: flex; gap: 18px; }
  .slider-arrows span { width: 44px; height: 44px; border-radius: 50%; display: flex; align-items: center; justify-content: center; border: 2px solid var(--line); }
  .slider-arrows span.is-active { background: var(--navy); border-color: var(--navy); }

  /* ---------- footer ---------- */
  .site-footer { position: absolute; top: 2340px; left: 0; width: 1200px; height: 276px; color: var(--white); }
  .footer-bg { position: absolute; inset: 0; }
  .footer-brand { position: absolute; left: 120px; top: 66px; display: flex; align-items: center; gap: 14px; font-weight: 600; font-size: 28px; line-height: 1.1; letter-spacing: .5px; }
  .footer-brand .brand-dot { width: 52px; height: 52px; }
  .social { position: absolute; left: 200px; top: 172px; display: flex; gap: 10px; }
  .social span { width: 30px; height: 30px; border-radius: 50%; border: 2px solid var(--white); }
  .stay { position: absolute; left: 618px; top: 50px; width: 470px; }
  .stay h4 { font-weight: 400; font-size: 28px; }
  .stay p { font-size: 14px; line-height: 1.55; margin-top: 6px; opacity: .92; }
  .subscribe { display: flex; gap: 16px; margin-top: 18px; }
  .subscribe span { font-size: 12.5px; }
  .sub-input { width: 300px; height: 40px; border-radius: 20px; background: var(--white); color: #8a94a0; padding: 0 20px; display: flex; align-items: center; }
  .sub-btn { height: 40px; border-radius: 20px; border: 2px solid var(--white); padding: 0 26px; display: flex; align-items: center; letter-spacing: 2px; text-transform: uppercase; }
  .footer-bar { position: absolute; left: 0; bottom: 0; width: 100%; height: 44px; border-top: 1px solid rgba(255,255,255,.25); display: flex; align-items: center; justify-content: space-between; padding: 0 110px 0 112px; font-size: 12.5px; }
  .footer-links { display: flex; gap: 40px; list-style: none; }
</style>
</head>
<body>

<header class="hero">
  <div class="hero-photo" role="img" aria-label="Photo of a lighthouse silhouetted against a sunset sky"></div>
  <nav class="site-nav">
    <div class="brand"><span class="brand-dot"></span><span>BROOKVALE<br>ADVISORS LLC</span></div>
    <ul class="nav-links">
      <li><a href="#">Home</a></li>
      <li><a href="#">About</a></li>
      <li><a href="#">Services offered</a></li>
      <li><a href="#">Contact</a></li>
      <li><a href="#">Resources</a></li>
    </ul>
  </nav>
  <div class="hero-copy">
    <h1 class="hero-title">BROOKVALE<br>ADVISORS LLC</h1>
    <p class="hero-lead">I have spent my entire 35 year career in this industry, with the last 22 years...</p>
    <a class="btn-outline" href="#">Free Consulting</a>
  </div>
  <div class="hero-dots"><span class="is-active"></span><span></span><span></span></div>
</header>

<section class="about">
  <div class="about-text">
    <div class="eyebrow">About</div>
    <h2 class="about-title">Brookvale<br>Advisors LLC</h2>
    <p>Brookvale Advisors LLC is a consulting and recruiting firm that provides education, perspective, guidance, and assistance to financial advisors. Specifically, we are focused on serving two distinct profiles of client.</p>
    <p>First, we assist financial advisors as they explore, plan, and execute their professional journey to independence.</p>
    <a class="btn-solid" href="#">Read More</a>
  </div>
  <div class="about-photo" role="img" aria-label="Portrait photo of founder Dennis Halloway"></div>
</section>

<section class="offers">
  <svg class="offers-bg" width="1200" height="700" viewBox="0 0 1200 700" role="img" aria-label="Photo of a calm beach at dusk in deep blue tones">
    <defs>
      <linearGradient id="offersTone" x1="0" y1="0" x2="0" y2="1">
        <stop offset="0" stop-color="#0f3d6c"/>
        <stop offset=".5" stop-color="#1b5586"/>
        <stop offset="1" stop-color="#0a2748"/>
      </linearGradient>
    </defs>
    <path d="M0 60 Q600 -30 1200 60 L1200 640 Q600 720 0 640 Z" fill="url(#offersTone)"/>
  </svg>
  <div class="offers-heading"><div class="small">Brookvale Advisors</div><div class="big">OFFER'S</div></div>

  <article class="offer" style="left:130px">
    <div class="offer-ring">
      <div class="offer-photo" role="img" aria-label="Photo of a hand writing notes in an open book" style="background:linear-gradient(135deg,#d8c3a5,#8a6b4c 60%,#4a3a2c)"></div>
      <svg width="240" height="240" viewBox="0 0 240 240" aria-hidden="true"><path d="M120 4 A116 116 0 1 1 14 168" fill="none" stroke="#fff" stroke-width="8"/></svg>
    </div>
    <h3>EDUCATION PERSPECTIVE</h3>
    <p>We help advisors understand every option for independence, from custody and compliance to technology, so each decision is made with clear eyes.</p>
    <a href="#">Read More</a>
  </article>

  <article class="offer" style="left:450px">
    <div class="offer-ring">
      <div class="offer-photo" role="img" aria-label="Photo of a team meeting around a table" style="background:linear-gradient(135deg,#e6e9ec,#9aa4ad 55%,#4c5863)"></div>
      <svg width="240" height="240" viewBox="0 0 240 240" aria-hidden="true"><path d="M120 4 A116 116 0 1 1 14 168" fill="none" stroke="#fff" stroke-width="8"/></svg>
    </div>
    <h3>ASSISTANCE</h3>
    <p>Hands-on support through every step of the transition, from business planning and contracts to moving clients and building your new team.</p>
    <a href="#">Read More</a>
  </article>

  <article class="offer" style="left:770px">
    <div class="offer-ring">
      <div class="offer-photo" role="img" aria-label="Photo of an advisor in conversation with a client" style="background:linear-gradient(135deg,#eceff2,#a9b2bb 55%,#2e3a47)"></div>
      <svg width="240" height="240" viewBox="0 0 240 240" aria-hidden="true"><path d="M120 4 A116 116 0 1 1 14 168" fill="none" stroke="#fff" stroke-width="8"/></svg>
    </div>
    <h3>FINANCIAL ADVISORS</h3>
    <p>We introduce experienced advisors to independent firms that fit their values, their clients and the way they want to run a practice.</p>
    <a href="#">Read More</a>
  </article>
</section>

<section class="clients">
  <div class="clients-heading"><div class="small">Brookvale Advisors</div><div class="big">WHAT OUR CLIENTS SAY</div></div>

  <blockquote class="quote-card" style="left:100px">
    <div class="quote-head"><div class="avatar" role="img" aria-label="Client portrait photo"></div><div><div class="quote-name">MARLA J DENTON</div><div class="quote-role">Independent Advisor</div></div></div>
    <p>Dennis walked me through each step of going independent. His guidance saved months of guesswork and my clients followed me gladly.</p>
  </blockquote>
  <blockquote class="quote-card" style="left:440px">
    <div class="quote-head"><div class="avatar" role="img" aria-label="Client portrait photo"></div><div><div class="quote-name">MARLA J DENTON</div><div class="quote-role">Independent Advisor</div></div></div>
    <p>Clear advice, honest answers and real follow-through. I finally own my practice and I could not have done it alone.</p>
  </blockquote>
  <blockquote class="quote-card" style="left:780px">
    <div class="quote-head"><div class="avatar" role="img" aria-label="Client portrait photo"></div><div><div class="quote-name">MARLA J DENTON</div><div class="quote-role">Independent Advisor</div></div></div>
    <p>After twenty years at a large firm I was unsure where to start. Brookvale gave me a plan and the confidence to act.</p>
  </blockquote>

  <div class="slider-arrows">
    <span><svg width="14" height="14" viewBox="0 0 14 14" aria-hidden="true"><path d="M9 2 L4 7 L9 12" fill="none" stroke="#0a2748" stroke-width="2"/></svg></span>
    <span class="is-active"><svg width="14" height="14" viewBox="0 0 14 14" aria-hidden="true"><path d="M5 2 L10 7 L5 12" fill="none" stroke="#fff" stroke-width="2"/></svg></span>
  </div>
</section>

<footer class="site-footer">
  <svg class="footer-bg" width="1200" height="276" viewBox="0 0 1200 276" aria-hidden="true">
    <path d="M0 30 Q600 -20 1200 30 L1200 276 L0 276 Z" fill="#0a2748"/>
  </svg>
  <div class="footer-brand"><span class="brand-dot"></span><span>BROOKVALE<br>ADVISORS LLC</span></div>
  <div class="social"><span></span><span></span><span></span><span></span></div>
  <div class="stay">
    <h4>Stay In Touch</h4>
    <p>Neque porro quisquam est qui dolorem ipsum quia dolor sit amet, consectetur, adipisci velit...</p>
    <div class="subscribe">
      <div class="sub-input"><span>Enter Your email</span></div>
      <div class="sub-btn"><span>Subscribe</span></div>
    </div>
  </div>
  <div class="footer-bar">
    <span>Brookvale Advisors LLC © 2021 All Rights Reserved.</span>
    <ul class="footer-links"><li>Home</li><li>About</li><li>Services offered</li><li>Contact</li><li>Resources</li></ul>
  </div>
</footer>

</body>
</html>
```